Plumber needs a business card

I need a new business card for my plumbing business. I dont have a logo at the moment but I want business cards that are simple but very professional. I want to look like
Name: Mitch Dorley
Address: (just make one up)
Phone: 0455 318 726
Email: mitch@dorleymail.com
Colors to use:
Blacks, blues, silvers

```html
<!DOCTYPE html>
<html lang="en">
<head>
<meta charset="UTF-8">
<title>Mitch Dorley – Business Card</title>
<link href="https://fonts.googleapis.com/css2?family=Lato:wght@400;700;900&display=swap" rel="stylesheet">
<style>
  :root {
    --backdrop: #c4c4c4;
    --card-black: #101010;
    --card-centre: #181818;
    --frame-blue: #3b56b0;
    --name-ink: #2c2c2c;
    --name-highlight: rgba(255, 255, 255, 0.28);
    --name-shadow: rgba(0, 0, 0, 0.95);
    --detail-grey: #8e8e8e;
  }
  * { margin: 0; padding: 0; box-sizing: border-box; }
  html, body {
    width: 1200px;
    height: 900px;
    overflow: hidden;
  }
  body {
    background: var(--backdrop);
    font-family: "Lato", sans-serif;
    position: relative;
  }
  .business-card {
    position: absolute;
    left: 172px;
    top: 206px;
    width: 857px;
    height: 488px;
    border: 6px solid var(--frame-blue);
    background: radial-gradient(ellipse at 50% 45%, var(--card-centre) 0%, var(--card-black) 70%);
    box-shadow: inset 0 0 0 1px #000;
  }
  .owner-name {
    position: absolute;
    top: 126px;
    left: 0;
    width: 100%;
    text-align: center;
    font-weight: 900;
    font-size: 46px;
    letter-spacing: -0.5px;
    color: var(--name-ink);
    text-shadow:
      -1px -1px 0 var(--name-highlight),
      1px 1px 0 #050505,
      3px 4px 5px var(--name-shadow);
  }
  .contact-details {
    position: absolute;
    top: 314px;
    left: 0;
    width: 100%;
    text-align: center;
    color: var(--detail-grey);
  }
  .business-address {
    font-size: 20px;
    line-height: 1;
    margin-bottom: 32px;
  }
  .phone-number {
    font-size: 21px;
    line-height: 1;
    margin-bottom: 7px;
  }
  .email-address {
    font-size: 20px;
    line-height: 1;
  }
</style>
</head>
<body>
  <section class="business-card">
    <h1 class="owner-name">Mitch Dorley</h1>
    <div class="contact-details">
      <p class="business-address">14 Kestrel Lane, Brookvale NSW 2100</p>
      <p class="phone-number">0455 318 726</p>
      <p class="email-address">mitch@dorleymail.com</p>
    </div>
  </section>
</body>
</html>
```